Bramble Spices "How to use" pamphlet - Bramble Nutrition LLC

We need a pamphlet/infographic flyer that shows users how to use our product. We are a hemp based cannabinoid nutrition company. The seasonings are made of high quality locally sourced organic ingredients from the beautiful state of Colorado and we want the design to emulate this message. The flyer should have 4-5 simple steps. Open the box, shake the seasoning well, pinch and sprinkle to taste, enjoy!
There will need to be a front and back to the design. The front or inside of the pamphlet will be the picture instructions on how to use. On the backside we want one section with the bramble nutrition logo, website and Instagram information. We also want to list great ways to pair the seasonings with food. The recommendation from Bramble is to use the product with healthy fats such as coconut oil, avocado, oil oil, ghee butter, salmon, etc.
Updates

Project Deadline Extended Reason: The brief was not able to be filled out until today. We want to extend the deadline to get a legitimate amount of time to get responses.Tim Added Thursday, September 7, 2017

Target Market(s)

We want to target those who are interested in hemp and how it can benefit overall health and wellbeing.

Industry/Entity Type

Nutrition

Font styles to use
Sans Serif

Colors
00a990
ecf7fb
fce8d3
85cae6

Requirements
Must have
• Simple infographics that explain the actions of how people use our seasons. Almost like a picture book.
• Maybe tri or quad fold layout. 2-3inches in height by 8 inches wide
• Clearly show where to find more information on Bramble: website, Instagram, etc
Nice to have
• Black, charcoal, white would be great colors. The pamphlet should be simple and easy to follow.
Should not have
• lots of text

```html
<!DOCTYPE html>
<html lang="en">
<head>
<meta charset="utf-8">
<title>Bramble Spices – How to Use Pamphlet</title>
<link rel="stylesheet" href="https://fonts.googleapis.com/css2?family=Open+Sans:wght@400;600&family=Oswald:wght@500&display=swap">
<style>
  :root{
    --teal:#00a990;
    --teal-dark:#00866f;
    --charcoal:#262626;
    --paper:#ffffff;
    --backdrop:#eeeaea;
    --wood-light:#d9b27a;
    --wood-dark:#8a5f33;
    --forest:#2f4a3a;
  }
  *{box-sizing:border-box;margin:0;padding:0}
  html,body{width:1200px;height:800px;overflow:hidden;background:var(--backdrop);font-family:"Open Sans",sans-serif}
  .canvas{position:relative;width:1200px;height:800px}

  .sheet{position:absolute;left:60px;width:1080px;height:350px;display:flex;box-shadow:0 6px 18px rgba(0,0,0,.18)}
  .sheet--inside{top:30px;background:var(--paper)}
  .sheet--outside{top:420px;background:var(--charcoal)}

  /* inside */
  .panel{position:relative;width:360px;height:100%;overflow:hidden}
  .panel + .panel{border-left:1px solid rgba(0,0,0,.08)}
  .step-band{position:absolute;left:0;right:0;height:36px;background:var(--teal);color:#fff;font-size:22px;padding-left:20px;line-height:36px}
  .step-icon{position:absolute;left:50%;transform:translateX(-50%)}
  .step-caption{position:absolute;left:0;right:0;text-align:center;color:var(--teal);font-size:17px;line-height:22px}
  .pairing-band{position:absolute;left:0;bottom:0;width:720px;height:70px;background:var(--teal);color:#fff;padding:10px 22px;z-index:2}
  .pairing-band .lead{font-size:12px;line-height:16px}
  .pairing-band .foods{font-size:21px;line-height:30px;margin-top:2px}
  .photo{position:absolute;background:linear-gradient(135deg,var(--wood-light),var(--wood-dark))}
  .photo-band{position:absolute;left:0;right:0;bottom:0;height:70px;background:var(--teal)}

  /* outside */
  .name-badge{position:absolute;border-radius:50%;background:var(--forest);display:flex;align-items:center;justify-content:center;text-align:center;color:#fff;font-family:"Oswald",sans-serif;font-weight:500;letter-spacing:2px}
  .name-badge--large{left:105px;top:25px;width:150px;height:150px;font-size:20px}
  .name-badge--small{right:25px;bottom:18px;width:110px;height:110px;font-size:15px}
  .outside-art{position:absolute;left:360px;top:0}
  .contact{position:absolute;left:760px;top:262px;color:var(--teal);font-size:12px;line-height:20px}
  .contact li{list-style:none;display:flex;align-items:center;gap:6px}
  .contact .dot{width:8px;height:8px;background:var(--teal);border-radius:50%}
  .contact .sq{width:8px;height:8px;background:var(--teal)}
</style>
</head>
<body>
<main class="canvas">

  <section class="sheet sheet--inside" aria-label="Pamphlet inside">
    <div class="panel">
      <div class="step-band" style="top:0">Step1</div>
      <svg class="step-icon" style="top:44px" width="80" height="70" viewBox="0 0 90 80" fill="none" stroke="#00a990" stroke-width="4" stroke-linejoin="round">
        <path d="M15 30 L45 42 L75 30 L75 62 L45 76 L15 62 Z"/>
        <path d="M45 42 L45 76"/>
        <path d="M15 30 L5 18 L35 8 L45 20 M75 30 L85 18 L55 8 L45 20"/>
      </svg>
      <p class="step-caption" style="top:118px">Open the box</p>
      <div class="step-band" style="top:148px">Step2</div>
      <svg class="step-icon" style="top:190px" width="110" height="52" viewBox="0 0 120 60" fill="none" stroke="#00a990" stroke-width="3">
        <rect x="38" y="8" width="44" height="40" transform="rotate(25 60 28)"/>
        <path d="M22 18 q-8 12 0 24 M14 14 q-12 16 0 32 M98 18 q8 12 0 24 M106 14 q12 16 0 32"/>
      </svg>
      <p class="step-caption" style="top:246px">Shake the seasoning well</p>
    </div>

    <div class="panel">
      <div class="step-band" style="top:0">Step3</div>
      <svg class="step-icon" style="top:44px" width="70" height="70" viewBox="0 0 80 80" fill="none" stroke="#00a990" stroke-width="3">
        <circle cx="40" cy="12" r="6" fill="#00a990" stroke="none"/>
        <path d="M40 20 L40 34"/>
        <rect x="18" y="42" width="44" height="30"/>
        <path d="M18 52 H62"/>
      </svg>
      <p class="step-caption" style="top:118px">Pinch</p>
      <div class="step-band" style="top:148px">Step4</div>
      <svg class="step-icon" style="top:192px" width="80" height="50" viewBox="0 0 80 50" fill="#00a990">
        <circle cx="40" cy="6" r="6"/>
        <circle cx="36" cy="20" r="2"/><circle cx="44" cy="24" r="2"/><circle cx="38" cy="31" r="2"/>
        <circle cx="30" cy="38" r="2"/><circle cx="46" cy="40" r="2"/><circle cx="40" cy="46" r="2"/>
      </svg>
      <p class="step-caption" style="top:246px">Sprinkle to taste, enjoy!</p>
    </div>

    <div class="panel">
      <div class="photo" role="img" aria-label="Photo of an open jar of seasoning with its label lid on a wooden table" style="inset:0 0 70px 0"></div>
      <div class="photo-band"></div>
    </div>

    <div class="pairing-band">
      <p class="lead">The recommendation from Bramble is to use the product with healthy fats such as</p>
      <p class="foods">coconut oil, avocado, oil oil, ghee butter, salmon, etc.</p>
    </div>
  </section>

  <section class="sheet sheet--outside" aria-label="Pamphlet outside">
    <div class="panel">
      <div class="name-badge name-badge--large">BRAMBLE<br>SPICES</div>
    </div>
    <svg class="outside-art" width="720" height="350" viewBox="0 0 720 350">
      <path d="M40 0 C 20 130, 150 240, 420 236 L720 236 L720 0 Z" fill="#00a990"/>
      <path d="M68 0 C 55 115, 170 222, 430 220 L720 220 L720 0 Z" fill="#00866f"/>
      <path d="M92 0 C 85 105, 190 208, 440 206 L720 206 L720 0 Z" fill="#c89a63" role="img" aria-label="Photo of a seasoning jar with label lid on a wooden table"/>
    </svg>
    <ul class="contact">
      <li><span class="dot"></span>www.bramblespices.com</li>
      <li><span class="sq"></span>/bramblespices</li>
    </ul>
    <div class="name-badge name-badge--small">BRAMBLE<br>SPICES</div>
  </section>

</main>
</body>
</html>
```